Vibrant, yet professional, stationery set and other designs required.

I need to source a fantastic designer for a new project as part of my company using a new logo designed via pixel forum.

**UPDATE** I am not looking for just 'fine' design that will suffice. I am looking for something great.

We are a life assurance brokerage based in Dublin, Ireland and BrightOak.ie is our new website aimed at providing services for young families in Ireland. We are hoping to be the 'Orvo' level of service providers in this area and I am looking for the quality of design to reflect this :-) Hopefully that makes sense!

I have a preference for straight lines over curves and waves.

I need...

1. Business card
2. Letterhead
3. Banner (for printing - 76cm X 305cm)
4. Car branding for ZENTA 300 (2014 sport model) I believe the templates are freely available online.

Target Market(s)

Parents in Ireland - Aged 27 to 50.

Industry/Entity Type

Financial Planning

Colors

Designer to choose colors to be used in the design.

Requirements
Must have
• All of the items listed in the description above. I like clean, bright, legible, vibrant and professional design.
Should not have
• No silly or 'cheap' looking designs. This is a professional company looking to provide a professional service.

```html
<!DOCTYPE html>
<html lang="en">
<head>
<meta charset="utf-8">
<title>BrightOak.ie – Business Card</title>
<link href="https://fonts.googleapis.com/css2?family=Source+Sans+3:wght@400;600;700&display=swap" rel="stylesheet">
<style>
  :root {
    --bg: #ecebe8;
    --card-white: #ffffff;
    --slate: #7a9097;
    --logo-grey: #6f8288;
    --green: #7cbc14;
    --blue: #23a6dc;
    --ink: #4a4f52;
  }
  * { box-sizing: border-box; margin: 0; padding: 0; }
  html, body { width: 1200px; height: 800px; overflow: hidden; }
  body {
    background: var(--bg);
    font-family: "Source Sans 3", "Myriad Pro", Arial, sans-serif;
    position: relative;
  }
  .card {
    position: absolute;
    top: 250px;
    width: 520px;
    height: 300px;
    box-shadow: 0 6px 18px rgba(0,0,0,.15);
    overflow: hidden;
  }
  .card--front { left: 50px; background: var(--card-white); }
  .card--back { left: 630px; background: var(--slate); }

  .identity {
    position: absolute;
    top: 44px;
    right: 118px;
    text-align: right;
    line-height: 1.05;
  }
  .identity__name { color: var(--blue); font-weight: 600; font-size: 19px; }
  .identity__role { color: var(--green); font-weight: 400; font-size: 16px; }

  .avatar-badge {
    position: absolute;
    top: 22px;
    right: 34px;
    width: 68px;
    height: 68px;
    border-radius: 50%;
    background: var(--green);
  }
  .avatar-badge svg { position: absolute; top: 20px; left: 20px; }

  .contact-tab {
    position: absolute;
    top: 104px;
    right: 0;
    width: 62px;
    height: 196px;
    background: var(--green);
    border-radius: 8px 0 0 0;
  }
  .contact-tab svg { position: absolute; left: 21px; }

  .contact {
    position: absolute;
    top: 124px;
    right: 78px;
    text-align: right;
    color: var(--ink);
    font-size: 14px;
    line-height: 20px;
  }
  .contact__gap { height: 14px; }

  .brand {
    position: absolute;
    display: flex;
    align-items: center;
    gap: 12px;
    font-weight: 700;
    letter-spacing: -0.5px;
  }
  .brand__dot { border-radius: 50%; flex: none; }
  .card--front .brand { left: 36px; bottom: 48px; font-size: 50px; color: var(--logo-grey); }
  .card--front .brand__dot { width: 20px; height: 20px; background: var(--green); }
  .card--back .brand {
    left: 0; right: 0; top: 0; bottom: 0;
    justify-content: center;
    font-size: 66px;
    color: #ffffff;
  }
  .card--back .brand__dot { width: 24px; height: 24px; background: #ffffff; }
</style>
</head>
<body>
  <section class="card card--front">
    <div class="identity">
      <p class="identity__name">DARA WHELAN</p>
      <p class="identity__role">CEO/FOUNDER</p>
    </div>

    <div class="avatar-badge">
      <svg width="28" height="28" viewBox="0 0 28 28" aria-hidden="true">
        <circle cx="14" cy="9" r="6" fill="#fff"/>
        <path d="M3 26c0-6 5-10 11-10s11 4 11 10z" fill="#fff"/>
      </svg>
    </div>

    <div class="contact-tab">
      <svg style="top:22px" width="18" height="20" viewBox="0 0 18 20" aria-hidden="true">
        <path d="M9 1a6 6 0 0 1 6 6c0 5-6 12-6 12S3 12 3 7a6 6 0 0 1 6-6z" fill="#fff"/>
        <circle cx="9" cy="7" r="2.2" fill="#7cbc14"/>
      </svg>
      <svg style="top:62px" width="18" height="16" viewBox="0 0 18 16" aria-hidden="true">
        <path d="M1 5c0-3 16-3 16 0v2h-4V5H5v2H1z" fill="#fff"/>
        <rect x="3" y="8" width="12" height="7" rx="1.5" fill="#fff"/>
      </svg>
      <svg style="top:86px" width="18" height="20" viewBox="0 0 18 20" aria-hidden="true">
        <rect x="4" y="1" width="10" height="18" rx="2" fill="none" stroke="#fff" stroke-width="2"/>
      </svg>
      <svg style="top:114px" width="18" height="14" viewBox="0 0 18 14" aria-hidden="true">
        <rect x="1" y="1" width="16" height="12" rx="1" fill="#fff"/>
        <path d="M1 2l8 6 8-6" fill="none" stroke="#7cbc14" stroke-width="1.5"/>
      </svg>
      <svg style="top:140px" width="18" height="18" viewBox="0 0 18 18" aria-hidden="true">
        <circle cx="9" cy="9" r="8" fill="#fff"/>
        <path d="M1 9h16M9 1c3 3 3 13 0 16M9 1c-3 3-3 13 0 16" fill="none" stroke="#7cbc14" stroke-width="1.2"/>
      </svg>
    </div>

    <div class="contact">
      <p>14 Hazel Court</p>
      <p>Rathmines, Dublin 6</p>
      <div class="contact__gap"></div>
      <p>601 555 0142</p>
      <p>601 555 0187</p>
      <p>601 555 0163</p>
      <p>hello@brightoak.ie</p>
      <p>www.brightoak.ie</p>
    </div>

    <div class="brand">
      <span class="brand__dot"></span>
      <span class="brand__name">BrightOak.ie</span>
    </div>
  </section>

  <section class="card card--back">
    <div class="brand">
      <span class="brand__dot"></span>
      <span class="brand__name">BrightOak.ie</span>
    </div>
  </section>
</body>
</html>
```